BRIGHT PEAK POWER.

I'd like my business logo.
contact name: Daniel Fitzhume
phone:0407395182
email: info@brightpeakpower.net.au
website: www.brightpeakpower.net.au

services:
solar
battery storage
LED lighting
energy saving solutions
general electrical
I'd like the design to look professional

Target Market(s)

Everyone

Industry/Entity Type

Business

Contact Information for Business Card

as described above

Requirements
Must have
• Id like the colours and the design to work well with my logo.

```html
<!DOCTYPE html>
<html lang="en">
<head>
<meta charset="utf-8">
<title>Bright Peak Power – Business Card</title>
<link rel="stylesheet" href="https://fonts.googleapis.com/css2?family=Open+Sans:wght@400;600;700&display=swap">
<style>
  :root {
    --page-bg: #ecebe8;
    --card-white: #ffffff;
    --green-light: #9acd3c;
    --green-mid: #7dbb2e;
    --green-dark: #5ca52a;
    --orange: #e8901a;
    --text-green: #74b52a;
    --shadow: rgba(0, 0, 0, 0.18);
  }
  * { box-sizing: border-box; margin: 0; padding: 0; }
  html, body {
    width: 1200px;
    height: 900px;
    overflow: hidden;
  }
  body {
    position: relative;
    background: var(--page-bg);
    font-family: "Open Sans", Arial, sans-serif;
  }
  .card {
    position: absolute;
    border-radius: 18px;
    overflow: hidden;
    box-shadow: 0 6px 18px var(--shadow);
  }

  /* Front */
  .card-front {
    left: 78px; top: 35px;
    width: 587px; height: 363px;
    background: var(--card-white);
  }
  .card-front .holder-name {
    position: absolute; top: 16px; left: 0; right: 0;
    text-align: center;
    color: var(--orange);
    font-weight: 600;
    font-size: 21px;
  }
  .card-front .brand-band {
    position: absolute; top: 60px; left: 0; right: 0; height: 80px;
    background: linear-gradient(180deg, var(--green-light), var(--green-dark));
  }
  .card-front .brand-disc {
    position: absolute; left: 227px; top: 52px;
    width: 134px; height: 134px; border-radius: 50%;
    background: var(--card-white);
  }
  .brand-name {
    position: absolute; left: 0; right: 0;
    text-align: center;
    font-weight: 700;
    letter-spacing: 2px;
  }
  .card-front .brand-name {
    top: 188px;
    font-size: 30px;
    color: var(--green-mid);
  }
  .card-front .contact {
    position: absolute; top: 270px; left: 0; right: 0;
    list-style: none;
    text-align: center;
    color: var(--text-green);
    font-size: 16px;
    line-height: 25px;
  }

  /* Back */
  .card-back {
    left: 390px; top: 507px;
    width: 565px; height: 348px;
    background: linear-gradient(180deg, var(--green-mid), var(--green-dark) 80%, var(--green-mid));
  }
  .card-back .white-band {
    position: absolute; top: 28px; left: 0; right: 0; height: 102px;
    background: var(--card-white);
  }
  .card-back .brand-disc {
    position: absolute; left: 201px; top: 12px;
    width: 144px; height: 144px; border-radius: 50%;
    background: var(--green-mid);
  }
  .card-back .brand-name {
    top: 160px;
    font-size: 30px;
    color: var(--card-white);
  }
  .card-back .services-title {
    position: absolute; top: 244px; left: 0; right: 0;
    text-align: center;
    color: var(--card-white);
    font-weight: 600;
    font-size: 17px;
  }
  .card-back .services {
    position: absolute; top: 280px; left: 0; right: 0;
    text-align: center;
    color: var(--card-white);
    font-weight: 600;
    font-size: 14px;
    line-height: 21px;
  }
  .services .sep {
    display: inline-block;
    width: 6px; height: 6px; border-radius: 50%;
    background: var(--card-white);
    margin: 0 6px;
    vertical-align: middle;
  }
</style>
</head>
<body>
  <section class="card card-front">
    <p class="holder-name">Daniel Fitzhume</p>
    <div class="brand-band"></div>
    <div class="brand-disc"></div>
    <p class="brand-name">BRIGHT PEAK POWER</p>
    <ul class="contact">
      <li>0407395182</li>
      <li>info@brightpeakpower.net.au</li>
      <li>www.brightpeakpower.net.au</li>
    </ul>
  </section>

  <section class="card card-back">
    <div class="white-band"></div>
    <div class="brand-disc"></div>
    <p class="brand-name">BRIGHT PEAK POWER</p>
    <p class="services-title">What I do</p>
    <p class="services">
      Solar<span class="sep"></span>Battery Storage<span class="sep"></span>LED Lighting<br>
      Energy Saving Solutions
    </p>
  </section>
</body>
</html>
```